Website for enterprise software start-up

We need a new Wordpress website. We are an early stage start-up focused on mobile video technology for cellular operators. The audience is strategy, marketing and customer acquisition execs from the operators.

The purpose of the site is to act as a sales brochure and capture leads. A demo app can be downloaded from the current site, want to put that behind a contact form.

Current website is at www.brellowmo.tv. Similar number of pages. Looking for a clean design template, with minimal customization. Blog will remain as is.

Want to be able to modify the copy via Wordpress. Reference designs I like: vandrisk.com, tallowquarrymetric.com

Target Market(s)

Mobile operators and MVNOs in the US and Asia Pacific regions

Industry/Entity Type

Business Software

Coding

Coded - Design and coding required

Number of Pages Required

4 page

Font styles to use
Sans Serif

Colors
f78f20

Requirements
Must have
• Form for downloading sample apps.
• Landing page with image, Product, Blog, About, Contact
• Team page

```html
<!DOCTYPE html>
<html lang="en">
<head>
<meta charset="utf-8">
<title>Brellowmo Media</title>
<link href="https://fonts.googleapis.com/css2?family=Mulish:wght@300;400;600;700&display=swap" rel="stylesheet">
<style>
:root{
  --orange:#f78f20;
  --dark:#333333;
  --darker:#262626;
  --white:#ffffff;
  --ink:#3a3a3a;
  --muted:#bdbdbd;
}
*{box-sizing:border-box;margin:0;padding:0}
html,body{width:1200px;height:3766px;overflow:hidden}
body{position:relative;font-family:"Mulish",sans-serif;font-weight:300;color:var(--ink);background:var(--white)}
.abs{position:absolute}
.backdrop{position:absolute;left:0;top:0}
.brand{display:flex;align-items:center;gap:10px;color:var(--white);font-weight:700;font-size:34px;letter-spacing:-0.5px}
.brand-mark{width:30px;height:30px;background:var(--orange)}
.nav{left:590px;top:44px;display:flex;gap:30px;font-size:13px;font-weight:600;color:var(--white);letter-spacing:.5px}
.nav .active{border-bottom:3px solid var(--orange);padding-bottom:10px}
.login{left:968px;top:40px;width:86px;height:32px;background:var(--orange);color:var(--white);font-size:13px;font-weight:600;display:flex;align-items:center;justify-content:center}
.hero-title{left:0;width:1200px;top:400px;text-align:center;font-size:44px;color:var(--white);font-weight:300}
.hero-title span{color:var(--orange)}
.hero-sub{left:0;width:1200px;top:468px;text-align:center;font-size:16px;color:var(--white)}
.play{left:558px;top:284px;width:84px;height:84px;border:4px solid var(--white);border-radius:50%}
.dots{left:552px;top:588px;display:flex;gap:10px}
.dots i{width:8px;height:8px;border-radius:50%;background:var(--white)}
.dots i:first-child{background:var(--orange)}
.phone{background:var(--white);border-radius:40px;box-shadow:0 6px 20px rgba(0,0,0,.25)}
.phone-screen{position:absolute}
.phone-btn{position:absolute;width:40px;height:40px;border:2px solid #ddd;border-radius:50%}
.phone-slot{position:absolute;width:44px;height:6px;border-radius:3px;background:#ccc}
.section-title{font-size:40px;font-weight:300;line-height:1.25}
.welcome{left:517px;top:735px;color:var(--white)}
.bullets{left:517px;top:870px;width:540px;list-style:none;color:var(--white);font-size:15px;line-height:1.6}
.bullets li{position:relative;padding-left:22px;margin-bottom:18px}
.bullets li::before{content:"›";position:absolute;left:0;top:-2px;font-size:18px}
.btn{display:flex;align-items:center;justify-content:center;font-size:14px;font-weight:600;color:var(--white);letter-spacing:.5px}
.btn-dark{background:var(--dark)}
.btn-orange{background:var(--orange)}
.available-title{left:208px;top:1355px;color:var(--orange)}
.available-copy{left:208px;top:1455px;width:420px;color:var(--white);font-size:19px;line-height:1.6}
.available-copy p{margin-bottom:22px}
.available-copy .accent{color:var(--orange)}
.platform{color:var(--white);font-weight:700;font-size:30px;display:flex;flex-direction:column;align-items:center;gap:10px}
.platform i{width:50px;height:50px;border-radius:50%;background:var(--white)}
.team-title{left:552px;top:1915px;color:var(--ink)}
.photo{position:absolute}
.member-card{left:145px;top:2258px;width:395px;height:498px;background:var(--dark);text-align:center;color:var(--white)}
.member-name{margin-top:50px;font-size:26px;color:var(--orange);font-weight:400}
.member-bio{margin:40px auto 0;width:300px;font-size:14px;line-height:1.8}
.name-badge{left:638px;top:2161px;width:70px;height:70px;border-radius:50%;background:var(--orange);color:var(--white);font-size:16px;display:flex;align-items:center;justify-content:center}
.contact-title{left:145px;top:2825px;color:var(--white)}
.field{background:var(--white);font-size:14px;color:#777;padding:18px 20px}
.partners{left:110px;top:3360px;width:980px;display:flex;justify-content:space-between;align-items:center}
.partner{font-size:18px;font-weight:700;color:#555}
.footer-col{font-size:12px;line-height:24px;color:var(--white);letter-spacing:.4px}
.footer-col h4{font-size:12px;font-weight:600;color:var(--orange);margin-bottom:10px}
.footer-rule{left:0;top:3712px;width:1200px;height:1px;background:#444}
.copyright{left:0;width:1200px;top:3727px;text-align:center;color:var(--white);font-size:12px;letter-spacing:.5px}
</style>
</head>
<body>

<svg class="backdrop" width="1200" height="3766" viewBox="0 0 1200 3766">
  <defs>
    <linearGradient id="heroTone" x1="0" y1="0" x2="1" y2="1">
      <stop offset="0" stop-color="#2a2624"/>
      <stop offset=".5" stop-color="#6b5f58"/>
      <stop offset="1" stop-color="#3b3532"/>
    </linearGradient>
    <linearGradient id="contactTone" x1="0" y1="0" x2="1" y2="1">
      <stop offset="0" stop-color="#f78f20"/>
      <stop offset="1" stop-color="#f39a3c"/>
    </linearGradient>
  </defs>
  <rect x="0" y="560" width="1200" height="800" fill="var(--orange)"/>
  <polygon points="0,1250 1200,1180 1200,1860 0,1930" fill="var(--dark)"/>
  <polygon points="0,2710 1200,2775 1200,3213 0,3265" fill="url(#contactTone)"/>
  <polygon points="0,3465 1200,3435 1200,3766 0,3766" fill="var(--dark)"/>
  <!-- arrow from featured photo toward the team grid -->
  <path d="M500,1985 C450,1985 420,2020 415,2070" fill="none" stroke="var(--ink)" stroke-width="3"/>
  <path d="M402,2052 L415,2072 L428,2052" fill="none" stroke="var(--ink)" stroke-width="3"/>
</svg>

<div class="abs" role="img" aria-label="Hero photo: a person holding a smartphone playing a video" style="left:0;top:0;width:1200px;height:680px;background:url(#) ,linear-gradient(135deg,#2a2624,#6b5f58 55%,#3b3532);clip-path:polygon(0 0,100% 0,100% 100%,0 88%)"></div>

<header>
  <div class="abs brand" style="left:146px;top:34px"><span class="brand-mark"></span>brellowmo</div>
  <nav class="abs nav">
    <span class="active">HOME</span><span>PRODUCT</span><span>CONTACT</span><span>BLOG</span><span>ABOUT</span>
  </nav>
  <div class="abs login">LOGIN</div>
</header>

<section class="hero">
  <div class="abs play"></div>
  <svg class="abs" style="left:588px;top:310px" width="30" height="34" viewBox="0 0 30 34"><polygon points="2,2 28,17 2,32" fill="var(--white)"/></svg>
  <h1 class="abs hero-title"><span>High Quality</span> Mobile Engagement™</h1>
  <p class="abs hero-sub">We engage mobile audiences with the right video content at the perfect moment</p>
  <div class="abs dots"><i></i><i></i><i></i><i></i></div>
</section>

<section class="welcome-section">
  <div class="abs phone" style="left:216px;top:695px;width:248px;height:520px">
    <span class="phone-slot" style="left:102px;top:38px"></span>
    <div class="phone-screen" role="img" aria-label="App screen showing a darkened video still" style="left:17px;top:73px;width:211px;height:367px;background:linear-gradient(180deg,#1e1e1e,#3c3c3c)">
      <div class="brand" style="position:absolute;left:28px;top:168px;font-size:22px"><span class="brand-mark" style="width:20px;height:20px"></span>brellowmo</div>
    </div>
    <span class="phone-btn" style="left:104px;top:460px"></span>
  </div>
  <h2 class="abs section-title welcome">Welcome to<br>Brellowmo Media</h2>
  <ul class="abs bullets">
    <li>Increase ARPU with new revenue streams.</li>
    <li>Brellowmo Media is a content platform for operators, that allows them to create new business models based on mobile video</li>
    <li>Brellowmo's platforms predictively pre-positions video content, and uses ML to reveal video at the perfect moment for maximum engagement</li>
  </ul>
  <div class="abs btn btn-dark" style="left:517px;top:1067px;width:228px;height:55px">GET STARTED TODAY !</div>
</section>

<section class="available-section">
  <h2 class="abs section-title available-title">Available In</h2>
  <div class="abs available-copy">
    <p>Videos are revealed at the right moment based on behavioral models that are built on the device.</p>
    <p>Theyappear as notifications, fullscreen videos, overlays or wallpapers.</p>
    <p class="accent">Works for both Aplos and Verdroid.</p>
  </div>
  <div class="abs btn btn-orange" style="left:206px;top:1725px;width:226px;height:55px">DOWNLOAD APP NOW</div>
  <div class="abs phone" style="left:745px;top:1260px;width:249px;height:522px">
    <span class="phone-slot" style="left:102px;top:38px"></span>
    <div class="phone-screen" style="left:20px;top:75px;width:211px;height:377px;background:var(--orange);display:flex;flex-direction:column;justify-content:center;align-items:center;gap:60px">
      <div class="platform"><i></i>Aplos</div>
      <div class="platform"><i></i>Verdroid</div>
    </div>
    <span class="phone-btn" style="left:104px;top:468px"></span>
  </div>
</section>

<section class="team-section">
  <h2 class="abs section-title team-title">Team</h2>
  <div class="photo" role="img" aria-label="Cut-out portrait of team member Rolf" style="left:200px;top:1945px;width:302px;height:315px;background:linear-gradient(180deg,#d9d4cf,#4a4a4a)"></div>
  <div class="abs member-card">
    <h3 class="member-name">Rolf</h3>
    <p class="member-bio">At vero eos et accusamus et iusto odio dignissimos ducimus qui blanditiis praesentium voluptatum deleniti atque corrupti quos dolores et quas molestias excepturi sint occaecati cupiditate non provident, similique sunt in culpa qui officia deserunt mollitia animi.</p>
    <div class="btn btn-orange" style="margin:30px auto 0;width:229px;height:52px">LEARN MORE</div>
  </div>
  <div class="photo" role="img" aria-label="Team member portrait, dimmed on hover" style="left:555px;top:2028px;width:233px;height:221px;background:linear-gradient(180deg,#6a6a6a,#3c3c3c)"></div>
  <div class="photo" role="img" aria-label="Team member portrait" style="left:800px;top:2028px;width:232px;height:221px;background:linear-gradient(180deg,#e4e2df,#8a8580)"></div>
  <div class="photo" role="img" aria-label="Team member portrait" style="left:555px;top:2259px;width:233px;height:221px;background:linear-gradient(180deg,#d6d3cf,#3d4a63)"></div>
  <div class="photo" role="img" aria-label="Team member portrait" style="left:800px;top:2259px;width:232px;height:221px;background:linear-gradient(180deg,#c9c4be,#6f6a66)"></div>
  <div class="photo" role="img" aria-label="Team member portrait" style="left:555px;top:2490px;width:233px;height:221px;background:linear-gradient(180deg,#e0ddda,#c23a36)"></div>
  <div class="photo" role="img" aria-label="Team member portrait" style="left:800px;top:2490px;width:232px;height:221px;background:linear-gradient(180deg,#e6e4e1,#3e4148)"></div>
  <div class="abs name-badge">Teodor</div>
</section>

<section class="contact-section">
  <h2 class="abs section-title contact-title">Contact Us</h2>
  <div class="abs field" style="left:145px;top:2917px;width:442px;height:55px">Name</div>
  <div class="abs field" style="left:145px;top:2994px;width:442px;height:56px">E-mail</div>
  <div class="abs field" style="left:145px;top:3070px;width:442px;height:55px">Subject</div>
  <div class="abs field" style="left:610px;top:2917px;width:442px;height:208px">Message</div>
  <div class="abs btn btn-dark" style="left:145px;top:3150px;width:131px;height:55px">SEND</div>
</section>

<section class="abs partners">
  <span class="partner">Lumenvale</span>
  <span class="partner">Harborline</span>
  <span class="partner">Quillora</span>
  <span class="partner">Tessmark</span>
  <span class="partner">Orbisfield</span>
  <span class="partner">Corvanta</span>
  <span class="partner">Dunmere Records</span>
</section>

<footer>
  <div class="abs brand" style="left:145px;top:3505px"><span class="brand-mark"></span>brellowmo</div>
  <div class="abs footer-col" style="left:402px;top:3505px">
    <h4>QUICK LINKS</h4>HOME<br>PRODUCT<br>CONTACT<br>BLOG<br>ABOUT
  </div>
  <div class="abs footer-col" style="left:570px;top:3505px">
    <h4>OTHER LINKS</h4>TERMS OF SERVICE<br>PRIVACY POLICY<br>COOKIES<br>HELP
  </div>
  <div class="abs footer-col" style="left:760px;top:3505px">
    <h4>CONTACT US</h4>KESTRELHAUS<br>LINDENWEG 42<br>10115 BERLIN<br>GERMANY<br>TELEPHONE: +49 30 5550 1928<br>E-MAIL: HELLO@BRELLOWMO.TV
  </div>
  <div class="abs footer-rule"></div>
  <p class="abs copyright">© 2016 COMPANY NAME &nbsp;|&nbsp; ALL RIGHTS RESERVED</p>
</footer>

</body>
</html>
```